New Stationery Design Project

Hi, I am a trial attorney in Harbor Point, California. I just had a logo designed through artforge and am ready for business cards and stationery.
I’d like a letterpress style business card with foil stamping on certain features. I'd like letterpress stationery that complements the business card.
I think I’d like the back of the card with the solid blue color and the front to be white.
However, I would like to see a version that is solid blue on the front and back. Feel free to be creative.
The contact information on it would include:
Name: Marco Villaseñor, Trial Attorney
Locations: Harbor Point | Mesa Linda
Phone number: 555.555.0172
Email: marco@villasenorlegalpros.example
Website: www.villasenorlegalpros.example
I would like a design that uses the same colors and font as my logo. The color is #04273D and the fonts are Mrs.Eaves and Gotham.
I've attached a file with my logo and some business cards I like (embossed and letterpress). There is also a monogram letter than can be used in the design.
The final design should communicate professionalism with a classic touch. I want people that interact with my cards and stationery to see a simple, clean and timeless design with a modern twist. I want them to feel that the legal work--through my business card and stationery--have value, are timeless, and are handcrafted to their personal needs.
Thanks!
Marco
Updates
I have provided vector files for the logo and symbols. Thanks!
I've posted a picture of a card submission that I also like in terms of design (blue strip on the bottom of the front of the card and icon on the right hand side). Only issue is I don't necessarily like the layout. Can someone recommend a better layout for the content? Thanks.
Target Market(s)
Small to mediums size companies.
Industry/Entity Type
Business
Look and feel

```html
<!DOCTYPE html>
<html lang="en">
<head>
<meta charset="utf-8">
<title>Villaseñor Business Cards</title>
<link rel="stylesheet" href="https://fonts.googleapis.com/css2?family=Libre+Baskerville:wght@400;700&family=Lato:wght@300;400&display=swap">
<style>
  :root {
    --backdrop: #e9e8e4;
    --navy: #0c2840;
    --paper-white: #ffffff;
    --detail-grey: #a9b3bd;
    --monogram-fill: #2b4760;
    --card-shadow: rgba(10, 20, 30, 0.22);
  }
  * { box-sizing: border-box; margin: 0; padding: 0; }
  html, body {
    width: 1200px;
    height: 902px;
    overflow: hidden;
    background: var(--backdrop);
  }
  .sheet {
    width: 1200px;
    height: 902px;
    display: flex;
    align-items: center;
    justify-content: center;
    gap: 44px;
  }
  .card {
    width: 520px;
    height: 298px;
    background: var(--navy);
    box-shadow: 0 10px 28px var(--card-shadow);
    position: relative;
    overflow: hidden;
  }
  .card-front {
    display: flex;
    align-items: center;
    justify-content: center;
  }
  .wordmark {
    font-family: "Libre Baskerville", serif;
    font-weight: 400;
    font-size: 30px;
    letter-spacing: 6px;
    color: var(--paper-white);
    text-transform: uppercase;
  }
  .card-back {
    padding: 46px 40px 0 44px;
    display: flex;
    gap: 26px;
  }
  .monogram-area {
    width: 96px;
    height: 88px;
    flex: none;
    background: var(--monogram-fill);
  }
  .contact { padding-top: 66px; }
  .contact-name {
    font-family: "Libre Baskerville", serif;
    font-weight: 700;
    font-size: 19px;
    color: var(--paper-white);
    margin-bottom: 12px;
  }
  .contact-lines {
    list-style: none;
    font-family: "Lato", sans-serif;
    font-weight: 300;
    font-size: 13px;
    line-height: 17px;
    color: var(--detail-grey);
  }
</style>
</head>
<body>
  <main class="sheet">
    <section class="card card-front" aria-label="Card front">
      <h1 class="wordmark">Villaseñor</h1>
    </section>
    <section class="card card-back" aria-label="Card back">
      <div class="monogram-area" role="img" aria-label="Monogram letter tile"></div>
      <div class="contact">
        <h2 class="contact-name">Marco Villaseñor</h2>
        <ul class="contact-lines">
          <li>Trial Attorney</li>
          <li>555.555.0172</li>
          <li>marco@villasenorlegalpros.example</li>
          <li>Harbor Point | Mesa Linda</li>
          <li>www.villasenorlegalpros.example</li>
        </ul>
      </div>
    </section>
  </main>
</body>
</html>
```